Tovenly Website Redesign

We have a web site called tovenly.com that is all about education/information about legal marijuana. We're looking to significantly improve the modern-ness and look/feel of the web site - and to make it look like many of the best web sites out there today.

The task will be to come up with a better design for:
- The home page: http://tovenly.com/
- The logo (see the logo at the top of each page)
- The header and footer (for all the pages)
- The vaporizer page: http://tovenly.com/collections/vaporizer
- The store map page: http://tovenly.com/pages/shop-marijuana-in-colorado-state

The output of the project will be:
- screenshots of the designs and any images needed
- PSD file

Key requirements:
- Style needs to look fresh/modern
- Especially on the vaporizers page, the key things we want to drive is conversion - getting more people to interact with the page and actually click on the links to purchase vaporizers

Reason: Raised the budget and want to give designers a few more days to provide entries.

Note I clarified that I don't need code (HTML or CSS) for the project. I just need the designs, including images and the PSD file. Thanks.

Reason: We're getting closet to selecting a design, just need a few more days to iterate on a few we're working on.

Industry/Entity Type

Education

Font styles to use
Sans Serif

Requirements
Must have
• Must look like a modern/clean/fresh looking website design.

```html
<!DOCTYPE html>
<html lang="en">
<head>
<meta charset="utf-8">
<title>Tovenly — Shop marijuana in style</title>
<link href="https://fonts.googleapis.com/css2?family=Open+Sans:wght@300;400;600;700&display=swap" rel="stylesheet">
<style>
:root{
  --green:#6bdc8a;
  --green-dark:#2fcc55;
  --green-text:#5fd47f;
  --ink:#333;
  --footer:#333;
  --footer-deep:#222;
  --white:#fff;
  --line:#e6e6e6;
  --thumb-leaf:#e3e9dc;
  --thumb-city:#9fb3bf;
  --thumb-tower:#b7c0c7;
}
*{margin:0;padding:0;box-sizing:border-box}
html,body{width:1200px;height:900px;overflow:hidden;background:var(--white);font-family:'Open Sans',sans-serif;color:var(--ink)}
.page{position:relative;width:1200px;height:900px}

/* header */
.site-header{position:absolute;left:0;top:0;width:1200px;height:47px;border-top:2px solid var(--green);background:linear-gradient(#fff,#f1f1f1)}
.brand{position:absolute;left:172px;top:2px;display:flex;align-items:baseline;gap:12px}
.brand-name{font-size:38px;font-weight:700;color:var(--green-dark);letter-spacing:3px;line-height:42px}
.brand-tag{font-size:11px;font-weight:600;color:#444}
.header-contact{position:absolute;right:172px;top:10px;text-align:right;font-size:9px;line-height:11px;color:#888}
.header-contact b{color:#777}

/* nav */
.main-nav{position:absolute;left:0;top:47px;width:1200px;height:26px;background:var(--green)}
.main-nav ul{list-style:none;position:absolute;left:172px;top:0;display:flex;height:26px}
.main-nav li{display:flex;align-items:center;gap:5px;padding-left:15px;font-size:10px;letter-spacing:.3px;color:var(--white);border-right:1px solid rgba(255,255,255,.35);height:26px}
.main-nav li.active{background:var(--green-dark)}
.main-nav svg{width:10px;height:10px;fill:#fff}

/* hero */
.hero{position:absolute;left:0;top:73px;width:1200px;height:200px;overflow:hidden}
.hero-photo{position:absolute;inset:0;background:linear-gradient(100deg,#c9a79a 0%,#e8cfc4 25%,#eef0f4 45%,#dfe6ee 65%,#f4f6f8 100%)}
.hero-title{position:absolute;left:597px;top:29px;white-space:nowrap;font-size:22px;font-weight:700;color:var(--white);letter-spacing:2.6px}
.hero-tag{position:absolute;height:22px;right:0;background:var(--green);color:var(--white);font-size:14px;line-height:22px;letter-spacing:.9px;white-space:nowrap;overflow:hidden}

/* intro band */
.intro{position:absolute;left:0;top:273px;width:1200px;height:73px;background:var(--green);color:var(--white)}
.intro-lead{position:absolute;left:172px;top:12px;font-size:19px;font-weight:300;line-height:20px;letter-spacing:.9px}
.intro-text{position:absolute;left:620px;top:13px;font-size:10px;line-height:11px;width:405px;letter-spacing:.2px}
.btn-outline{position:absolute;left:620px;top:43px;width:118px;height:18px;border:1px solid #fff;font-size:10px;line-height:16px;text-align:center;letter-spacing:.6px}

/* features */
.feature{position:absolute;top:361px;width:184px}
.feature h3{font-size:15px;font-weight:400;color:#555;margin-bottom:8px;letter-spacing:.3px}
.feature p{font-size:8.5px;line-height:10.2px;letter-spacing:.25px;color:#333}
.divider{position:absolute;left:172px;top:475px;width:856px;height:1px;background:var(--line)}

/* projects */
.projects-intro{position:absolute;left:172px;top:493px;width:178px}
.projects-intro h2{font-size:15px;font-weight:400;color:#555;margin-bottom:10px;letter-spacing:.3px}
.projects-intro p{font-size:8.5px;line-height:10.3px;letter-spacing:.25px}
.projects-intro a{display:block;margin-top:13px;font-size:8.5px;color:var(--green-text);text-decoration:none}
.carousel-arrows{position:absolute;left:994px;top:489px;font-size:13px;color:#555;letter-spacing:6px}
.project{position:absolute;top:506px;width:189px}
.project .thumb{height:80px}
.project p{margin-top:5px;font-size:10px;line-height:11px;letter-spacing:.35px;color:var(--green-text)}
.project.first{border-bottom:1px solid var(--line);padding-bottom:5px}

/* footer */
.site-footer{position:absolute;left:0;top:640px;width:1200px;height:225px;background:var(--footer);border-top:2px solid var(--green);color:#ddd}
.fcol{position:absolute;top:18px}
.fcol h4{font-size:10.5px;font-weight:400;color:#eee;margin-bottom:12px}
.about h4{font-size:21px;font-weight:700;letter-spacing:1.5px;color:#fff;margin:-6px 0 0}
.about p{font-size:8.5px;line-height:10.5px;width:172px;margin-bottom:9px;letter-spacing:.2px}
.social{display:flex;gap:8px;margin-top:10px}
.social span{width:30px;height:14px;display:flex;justify-content:center;border-bottom:2px solid}
.social i{width:9px;height:9px;border-radius:50%;background:#666}
.post{display:flex;gap:17px;height:41px}
.post .thumb{width:44px;height:23px;flex:none}
.post b{display:block;font-weight:400;font-size:9px;line-height:10px;color:#ddd;width:105px;letter-spacing:.2px}
.post small{display:block;font-size:6.5px;line-height:10px;color:#999}
.tweet{display:flex;gap:14px}
.tweet svg{flex:none;width:21px;height:13px;margin-top:2px}
.tweet p{font-size:8px;line-height:8.6px;width:125px;letter-spacing:.2px}
.tweet small{font-size:6px;color:#aaa}
.touch-row{display:flex;align-items:center;gap:14px;width:176px;border-bottom:1px solid #444;padding:3px 0 4px;font-size:8px;line-height:9.5px}
.touch-row svg{width:10px;height:10px;fill:#ccc;flex:none}
.touch-row span{border-left:1px solid #444;padding-left:8px;width:130px;letter-spacing:.2px}
.touch-row .strong{font-size:10.5px;font-weight:700;color:#fff}

.bottom-bar{position:absolute;left:0;top:865px;width:1200px;height:35px;background:var(--footer-deep);color:#ccc;font-size:8px;line-height:10px;letter-spacing:.2px;padding:7px 0 0 172px}
</style>
</head>
<body>
<div class="page">

<header class="site-header">
  <div class="brand"><span class="brand-name">Tovenly</span><span class="brand-tag">Shop marijuana in style</span></div>
  <div class="header-contact"><b>Call Toll Free :</b> 0000-0000- Lorem<br><b>e-mail :</b> info@tovenly.com</div>
</header>

<nav class="main-nav">
  <ul>
    <li class="active" style="width:78px"><svg viewBox="0 0 10 10"><path d="M5 1 0 5h1.5v4h2.5V6h2v3h2.5V5H10z"/></svg>Home</li>
    <li style="width:82px"><svg viewBox="0 0 10 10"><path d="M0 1h10v8H0zM1.5 3v1h7V3zm0 2v1h7V5z"/></svg>Blog</li>
    <li style="width:136px"><svg viewBox="0 0 10 10"><path d="M1 0h5l3 3v7H1z"/></svg>Marijuana 101</li>
    <li style="width:144px"><svg viewBox="0 0 10 10"><path d="M0 1h10v8H0zm1 1v6h8V2zm1 5 2-3 2 2 1-1 1 2z"/></svg>Legal Marijuana</li>
    <li style="width:127px"><svg viewBox="0 0 10 10"><circle cx="3.5" cy="5" r="3"/><circle cx="8" cy="3" r="2"/></svg>Vaporizers</li>
    <li style="width:110px;border-right:0"><svg viewBox="0 0 10 10"><path d="M0 2h10v6H0zm0 0 5 3.5L10 2"/></svg>Contact Us</li>
  </ul>
</nav>

<section class="hero">
  <div class="hero-photo" role="img" aria-label="Close-up photo of a hand holding a pen over printed charts"></div>
  <h1 class="hero-title">Lorem Ipsum is simply dummy text</h1>
  <div class="hero-tag" style="left:812px;top:71px;padding-left:33px">Lorem ipsum dolor sit amet, consectetur</div>
  <div class="hero-tag" style="left:845px;top:95px;padding-left:19px">There are many variations of passages</div>
  <div class="hero-tag" style="left:879px;top:119px;padding-left:13px">Lorem Ipsum is simply dummy text</div>
</section>

<section class="intro">
  <p class="intro-lead">Lorem ipsum dolor sit amet,<br>consectetur adipisicing elit</p>
  <p class="intro-text">Lorem Ipsum is simply dummy text of the printing and typesetting industry</p>
  <div class="btn-outline">READ MORE</div>
</section>

<section>
  <article class="feature" style="left:172px"><h3>Lorem Ipsum</h3><p>Lorem Ipsum is simply dummy text of the printing and typesetting industry. Lorem Ipsum has been the industry's standard dummy text ever since the 1500s</p></article>
  <article class="feature" style="left:397px"><h3>Lorem Ipsum</h3><p>Lorem Ipsum is simply dummy text of the printing and typesetting industry. Lorem Ipsum has been the industry's standard dummy text ever since the 1500s</p></article>
  <article class="feature" style="left:622px"><h3>Lorem Ipsum</h3><p>Lorem Ipsum is simply dummy text of the printing and typesetting industry. Lorem Ipsum has been the industry's standard dummy text ever since the 1500s</p></article>
  <article class="feature" style="left:847px"><h3>Lorem Ipsum</h3><p>Lorem Ipsum is simply dummy text of the printing and typesetting industry. Lorem Ipsum has been the industry's standard dummy text ever since the 1500s</p></article>
</section>
<div class="divider"></div>

<section>
  <div class="projects-intro"><h2>Recent Projects</h2><p>These are the recent works listed and for more works view full portfolio.</p><a href="#">view all portfolio</a></div>
  <div class="carousel-arrows">&lsaquo;&rsaquo;</div>
  <div class="project first" style="left:406px"><div class="thumb" role="img" aria-label="Photo of a cannabis leaf on white" style="background:var(--thumb-leaf)"></div><p>Ranking of vaporizers</p></div>
  <div class="project" style="left:616px"><div class="thumb" role="img" aria-label="Photo of a city skyline behind a park" style="background:var(--thumb-city)"></div><p>Map and ranking of Colorado Stores</p></div>
  <div class="project" style="left:826px"><div class="thumb" role="img" aria-label="Photo of a city skyline with a tower and mountains" style="background:var(--thumb-tower)"></div><p>Map of Washington State stores opening in July</p></div>
</section>

<footer class="site-footer">
  <div class="fcol about" style="left:172px">
    <h4>ABOUT US</h4>
    <p>Lorem Ipsum is simply dummy text of the printing and typesetting industry.</p>
    <p>Get in touch with us by following us on any of the social network.</p>
    <div class="social">
      <span style="border-bottom-color:#3b5998"><i></i></span>
      <span style="border-bottom-color:#3fa9e0"><i></i></span>
      <span style="border-bottom-color:#e0267a"><i></i></span>
      <span style="border-bottom-color:#f08a24"><i></i></span>
    </div>
  </div>
  <div class="fcol" style="left:391px">
    <h4>Recent Posts</h4>
    <div class="post"><div class="thumb" role="img" aria-label="Post thumbnail photo" style="background:#7d8a62"></div><div><b>Lorem ipsum dolor sit amet</b><small>Aug 12, 2014</small></div></div>
    <div class="post"><div class="thumb" role="img" aria-label="Post thumbnail photo" style="background:#3f6a98"></div><div><b>Lorem ipsum dolor sit amet</b><small>Aug 12, 2014</small></div></div>
    <div class="post"><div class="thumb" role="img" aria-label="Post thumbnail photo" style="background:#4d3a30"></div><div><b>Lorem ipsum dolor sit amet</b><small>Aug 12, 2014</small></div></div>
  </div>
  <div class="fcol" style="left:611px">
    <h4>Latest Twitts</h4>
    <div class="tweet" style="height:61px"><svg viewBox="0 0 21 13"><path d="M1 1h19v8H7l-4 3V9H1z" fill="#5fd47f"/></svg><p>Check out this great #Lorem ipsumLorem Ipsum is simply dummy text of the printing and typesetting industry.<br><small>- 0 days ago</small></p></div>
    <div class="tweet" style="height:53px"><svg viewBox="0 0 21 13"><path d="M1 1h19v8H7l-4 3V9H1z" fill="#5fd47f"/></svg><p>@Lorem ipsumLorem Ipsum is simply dummy text of the printing and typesetting industry.<br><small>- 0 days ago</small></p></div>
    <div class="tweet"><svg viewBox="0 0 21 13"><path d="M1 1h19v8H7l-4 3V9H1z" fill="#5fd47f"/></svg><p>@Lorem ipsumLorem Ipsum is simply dummy text of the printing and typesetting industry.<br><small>- 0 days ago</small></p></div>
  </div>
  <div class="fcol" style="left:831px">
    <h4>Get In Touch!</h4>
    <div class="touch-row"><svg viewBox="0 0 10 10"><path d="M5 1 0 5h1.5v4h2.5V6h2v3h2.5V5H10z"/></svg><span style="width:100px">Lorem Ipsum is simply dummy text</span></div>
    <div class="touch-row"><svg viewBox="0 0 10 10"><path d="M5 0a3.5 3.5 0 0 0-3.5 3.5C1.5 6 5 10 5 10s3.5-4 3.5-6.5A3.5 3.5 0 0 0 5 0zm0 5a1.5 1.5 0 1 1 0-3 1.5 1.5 0 0 1 0 3z"/></svg><span style="width:100px">Lorem Ipsum is simply dummy text</span></div>
    <div class="touch-row"><svg viewBox="0 0 10 10"><path d="M2 0 4 3 3 4.5C4 6.5 5 7 5.5 7L7 6l3 2-1 2C4 10 0 6 0 1z"/></svg><span class="strong">000 - 0123456789</span></div>
    <div class="touch-row"><svg viewBox="0 0 10 10"><path d="M0 2h10v6H0zm1 1 4 3 4-3"/></svg><span>contact@tovenly.com</span></div>
  </div>
</footer>

<div class="bottom-bar">© Copyright 2014 Tovenly - All Rights Reserved<br>contact@tovenly.com</div>

</div>
</body>
</html>
```